Kestrel Gardenworks Business Card

An eye catching, yet simple business card that includes;

1. our logo
2. office phone - 5083172946
3. email - kestrelgardenworks@mailbrook.com
4. website - www.kestrelgardenworks.com
5. instagram - @kestrelgardenworksnv

```html
<!DOCTYPE html>
<html lang="en">
<head>
<meta charset="UTF-8">
<title>Kestrel Gardenworks Business Card</title>
<link href="https://fonts.googleapis.com/css2?family=Poppins:wght@600;700&family=Open+Sans:wght@400&display=swap" rel="stylesheet">
<style>
  :root {
    --backdrop: #2a2a2a;
    --card: #0d0d0d;
    --copper: #a2622a;
    --white: #ffffff;
    --silver: #cfcfcf;
    --divider: #4a4a4a;
  }
  html, body {
    margin: 0;
    width: 1200px;
    height: 900px;
    overflow: hidden;
    background: var(--backdrop);
  }
  .sheet {
    position: relative;
    width: 1200px;
    height: 900px;
  }
  .card {
    position: absolute;
    left: 285px;
    width: 630px;
    height: 360px;
    border-radius: 22px;
    background: var(--card);
    overflow: hidden;
    box-shadow: 0 12px 30px rgba(0,0,0,0.5);
  }
  .card--front { top: 50px; }
  .card--back { top: 490px; }
  .card__swoosh {
    position: absolute;
    inset: 0;
    width: 100%;
    height: 100%;
  }
  .brand {
    position: absolute;
    display: flex;
    align-items: center;
    gap: 9px;
    font-family: "Poppins", sans-serif;
    font-weight: 700;
    line-height: 1;
    white-space: nowrap;
  }
  .brand__dot {
    width: 12px;
    height: 12px;
    border-radius: 50%;
    background: currentColor;
  }
  .card--front .brand { left: 34px; top: 150px; color: var(--copper); font-size: 19px; }
  .card--back .brand { left: 175px; top: 120px; color: var(--silver); font-size: 34px; }
  .divider {
    position: absolute;
    left: 302px;
    top: 52px;
    width: 1px;
    height: 160px;
    background: linear-gradient(var(--card), var(--divider), var(--card));
  }
  .contact {
    position: absolute;
    left: 324px;
    top: 54px;
    font-family: "Open Sans", sans-serif;
    color: var(--white);
  }
  .contact__name {
    margin: 0;
    font-family: "Poppins", sans-serif;
    font-weight: 600;
    font-size: 24px;
    color: var(--copper);
    line-height: 1.1;
  }
  .contact__title {
    margin: 2px 0 22px;
    font-size: 14px;
  }
  .contact__list {
    list-style: none;
    margin: 0;
    padding: 0;
    font-size: 13.5px;
  }
  .contact__item {
    display: flex;
    align-items: center;
    gap: 9px;
    margin-bottom: 5px;
  }
  .contact__icon {
    width: 14px;
    height: 14px;
    flex: none;
  }
  .website {
    font-family: "Open Sans", sans-serif;
    font-size: 16px;
    fill: var(--white);
  }
</style>
</head>
<body>
<main class="sheet">

  <section class="card card--front" aria-label="Card front">
    <svg class="card__swoosh" viewBox="0 0 630 360" aria-hidden="true">
      <path d="M110 360 C 280 290, 470 260, 630 250 L630 360 Z" fill="var(--copper)"/>
      <path d="M85 356 C 255 280, 440 245, 610 236" fill="none" stroke="var(--white)" stroke-width="3"/>
      <text class="website" transform="translate(330 342) rotate(-15)">www.kestrelgardenworks.com</text>
    </svg>

    <div class="brand"><span class="brand__dot"></span>Kestrel Gardenworks</div>

    <div class="divider"></div>

    <div class="contact">
      <h1 class="contact__name">Marcus Hale</h1>
      <p class="contact__title">Managing Director</p>
      <ul class="contact__list">
        <li class="contact__item">
          <svg class="contact__icon" viewBox="0 0 24 24"><path d="M6.6 10.8a15.1 15.1 0 0 0 6.6 6.6l2.2-2.2a1 1 0 0 1 1-.25 11.4 11.4 0 0 0 3.6.6 1 1 0 0 1 1 1V20a1 1 0 0 1-1 1A17 17 0 0 1 3 4a1 1 0 0 1 1-1h3.5a1 1 0 0 1 1 1c0 1.25.2 2.45.6 3.6a1 1 0 0 1-.25 1z" fill="var(--copper)"/></svg>
          5083172946
        </li>
        <li class="contact__item">
          <svg class="contact__icon" viewBox="0 0 24 24"><rect x="2" y="5" width="20" height="14" rx="1" fill="var(--copper)"/><path d="M2 6l10 7 10-7" fill="none" stroke="var(--card)" stroke-width="1.6"/></svg>
          kestrelgardenworks@mailbrook.com
        </li>
        <li class="contact__item">
          <svg class="contact__icon" viewBox="0 0 24 24"><circle cx="12" cy="12" r="9" fill="none" stroke="var(--copper)" stroke-width="2.4"/></svg>
          @kestrelgardenworksnv
        </li>
      </ul>
    </div>
  </section>

  <section class="card card--back" aria-label="Card back">
    <svg class="card__swoosh" viewBox="0 0 630 360" aria-hidden="true">
      <path d="M200 360 C 340 295, 490 270, 630 262 L630 360 Z" fill="var(--copper)"/>
      <path d="M172 356 C 315 285, 465 256, 610 248" fill="none" stroke="var(--white)" stroke-width="3"/>
      <text class="website" transform="translate(380 345) rotate(-13)">www.kestrelgardenworks.com</text>
    </svg>

    <div class="brand"><span class="brand__dot"></span>Kestrel Gardenworks</div>
  </section>

</main>
</body>
</html>
```